Telmoro Business Card

I already have the conplay logo. I need to develop a professional business card layout

Target Market(s)

Business

Industry/Entity Type

Business

Contact Information for Business Card

Company Name: Telmoro Limited

Font styles to use
Sans Serif

Colors

Designer to choose colors to be used in the design.

Requirements
Must have
• Use current logo
• Need two card size options:
• Small Card: 70mm x 28mm (Landscape)
• Square Card: 65mm x 65mm
Nice to have
• I will need 8-10 files for each name, number and email address (details to follow)

```html
<!DOCTYPE html>
<html lang="en">
<head>
<meta charset="utf-8">
<title>Telmoro Business Card</title>
<link rel="stylesheet" href="https://fonts.googleapis.com/css2?family=Montserrat:wght@400;600;800&display=swap">
<style>
  :root {
    --backdrop: #e9e4dc;
    --card: #161616;
    --card-edge: #2a2a2a;
    --text-light: #f2f2f2;
    --text-muted: #b8b8b8;
    --accent-red: #e8402f;
    --accent-orange: #f39a1e;
    --accent-yellow: #f4d21f;
    --accent-green: #6cc04a;
    --accent-cyan: #21b5e8;
    --accent-blue: #3f63d8;
    --accent-violet: #9b4fd0;
    --brand: #6cc04a;
  }
  * { box-sizing: border-box; margin: 0; padding: 0; }
  html, body { width: 773px; height: 1200px; overflow: hidden; }
  body {
    background: var(--backdrop);
    font-family: "Montserrat", sans-serif;
    display: flex;
    flex-direction: column;
    align-items: center;
    justify-content: center;
    gap: 110px;
  }
  .card {
    position: relative;
    background: var(--card);
    border: 1px solid var(--card-edge);
    border-radius: 4px;
    box-shadow: 0 14px 30px rgba(0,0,0,0.35);
    overflow: hidden;
  }
  /* Small card 70 x 28 mm */
  .card--small { width: 700px; height: 280px; }
  /* Square card 65 x 65 mm */
  .card--square { width: 560px; height: 560px; }
  .card__lines { position: absolute; inset: 0; width: 100%; height: 100%; }
  .brand {
    font-weight: 800;
    color: var(--brand);
    letter-spacing: 2px;
    text-transform: uppercase;
    white-space: nowrap;
  }
  .card--small .brand {
    position: absolute;
    left: 56px;
    top: 50%;
    transform: translateY(-50%);
    font-size: 38px;
  }
  .details {
    position: absolute;
    left: 360px;
    top: 50%;
    transform: translateY(-50%);
  }
  .person__name {
    color: var(--text-light);
    font-size: 20px;
    font-weight: 600;
    letter-spacing: 2px;
  }
  .person__title {
    color: var(--accent-yellow);
    font-size: 11px;
    letter-spacing: 4px;
    margin-top: 4px;
  }
  .contact {
    list-style: none;
    margin-top: 16px;
    color: var(--text-muted);
    font-size: 10px;
    line-height: 1.9;
  }
  .contact__item { display: flex; align-items: center; gap: 7px; white-space: nowrap; }
  .contact__dot { width: 6px; height: 6px; border-radius: 1px; }
  .card--square .brand {
    position: absolute;
    left: 0; right: 0;
    top: 50%;
    transform: translateY(-50%);
    text-align: center;
    font-size: 60px;
  }
</style>
</head>
<body>
  <section class="card card--small" aria-label="Small card with contact details">
    <svg class="card__lines" viewBox="0 0 700 280" aria-hidden="true">
      <line x1="540" y1="34" x2="670" y2="34" stroke="var(--accent-yellow)" stroke-width="2"/>
      <line x1="30" y1="246" x2="160" y2="246" stroke="var(--accent-cyan)" stroke-width="2"/>
      <line x1="330" y1="80" x2="330" y2="200" stroke="#333" stroke-width="1"/>
    </svg>
    <div class="brand">Telmoro</div>
    <div class="details">
      <div class="person__name">YOUR NAME</div>
      <div class="person__title">JOB TITLE</div>
      <ul class="contact">
        <li class="contact__item"><span class="contact__dot" style="background:var(--accent-red)"></span>12 Harbor Lane, City, ST 0000</li>
        <li class="contact__item"><span class="contact__dot" style="background:var(--accent-green)"></span>+1 555 010 2000</li>
        <li class="contact__item"><span class="contact__dot" style="background:var(--accent-cyan)"></span>hello@telmoro.com</li>
        <li class="contact__item"><span class="contact__dot" style="background:var(--accent-violet)"></span>www.telmoro.com</li>
      </ul>
    </div>
  </section>

  <section class="card card--square" aria-label="Square card with brand name">
    <svg class="card__lines" viewBox="0 0 560 560" aria-hidden="true">
      <line x1="360" y1="70" x2="400" y2="70" stroke="var(--accent-red)" stroke-width="2"/>
      <line x1="400" y1="70" x2="440" y2="70" stroke="var(--accent-orange)" stroke-width="2"/>
      <line x1="440" y1="70" x2="480" y2="70" stroke="var(--accent-yellow)" stroke-width="2"/>
      <line x1="480" y1="70" x2="520" y2="70" stroke="var(--accent-green)" stroke-width="2"/>
      <line x1="40" y1="490" x2="80" y2="490" stroke="var(--accent-cyan)" stroke-width="2"/>
      <line x1="80" y1="490" x2="120" y2="490" stroke="var(--accent-blue)" stroke-width="2"/>
      <line x1="120" y1="490" x2="160" y2="490" stroke="var(--accent-violet)" stroke-width="2"/>
      <line x1="160" y1="490" x2="200" y2="490" stroke="var(--accent-red)" stroke-width="2"/>
    </svg>
    <div class="brand">Telmoro</div>
  </section>
</body>
</html>
```